Menu Design Project for new restauranct concept

Design menu for new restaurant concept called Juniper's Burgers & Dogs. Logo is attached.

Industry/Entity Type

Restaurant

Requirements
Must have
• Menu items and pricing:

Burgers
Snack Burger $3.49
Snack Cheeseburger $3.99
Juniper's signature Burger $4.99
Juniper's signature Cheeseburger $5.49
Burger toppings: bacon, lettuce, tomato, onion, pickle, grilled onions, grilled mushrooms, grilled green peppers, jalapeƱo peppers.

Dogs
Hot Dog $2.99
Bacon Cheese Hot Dog $3.99
Slaw Dog $3.99
Kraut Dog $3.49
Chili Dog $3.99 with or with out cheese
Hot dogs are 100% beef

Other
Grilled Chicken Sandwich $5.99
Grilled Chicken Sandwich with cheese $6.49
(Same toppings as burgers)

French Fries $1.99

Loaded Potatos
The Plain Tater: $4.99 choose from: butter, sour cream, cheese, chives
The Garden Tater: $5.99 choose from: the Basic plus, broccoli & cheese, grilled mushrooms, onions, & peppers
The Rancher Tater: $6.99 choose from the Basic/Veggie plus: grilled chicken, chili, Philly cheesesteak, pulled pork.

Drinks
32oz. Drink $1.88
20oz. Drink $1.69

attached logo.
Nice to have
• love to incorporate the woodgrain backgound. It makes the logo look most like a cattle brand, which we like.

```html
<!DOCTYPE html>
<html lang="en">
<head>
<meta charset="utf-8">
<title>Juniper's Burgers &amp; Dogs — Menu</title>
<link rel="stylesheet" href="https://fonts.googleapis.com/css2?family=Passion+One:wght@400;700&family=Old+Standard+TT:wght@400;700&display=swap">
<style>
  :root{
    --backdrop:#242424;
    --wood-dark:#4a3220;
    --wood-mid:#7a5535;
    --wood-light:#94694a;
    --paper-light:#e2ddd1;
    --paper-mid:#cfc8b8;
    --paper-edge:#a79f8e;
    --ink:#2f2621;
    --ink-soft:#5a5048;
    --rule:#6b625a;
    --art-tan:#a8957a;
    --art-grey:#8f877c;
  }
  *{box-sizing:border-box;margin:0;padding:0}
  html,body{width:1200px;height:927px;overflow:hidden;background:var(--backdrop)}
  body{position:relative;font-family:"Old Standard TT",Georgia,serif;color:var(--ink)}

  .menu-page{position:absolute;top:95px;width:540px;height:740px}
  .menu-page--front{left:40px}
  .menu-page--back{left:620px}

  .wood-band{position:absolute;left:0;width:100%;
    background:linear-gradient(90deg,var(--wood-dark),var(--wood-mid) 30%,var(--wood-light) 55%,var(--wood-mid) 80%,var(--wood-dark))}
  .wood-band--top{top:0;height:70px}
  .wood-band--bottom{bottom:0;height:110px}

  .paper{position:absolute;left:0;top:45px;width:100%;height:610px;
    background:radial-gradient(ellipse at 50% 45%,var(--paper-light),var(--paper-mid) 70%,var(--paper-edge))}
  .paper-frame{position:absolute;inset:18px 22px;border:3px double var(--rule)}

  .band-name{position:absolute;bottom:22px;left:0;width:100%;text-align:center;
    font-family:"Passion One",Impact,sans-serif;font-weight:700;font-size:26px;color:var(--paper-mid);letter-spacing:.5px}

  .art{position:absolute;border-radius:6px}
  .art--lettering{background:linear-gradient(135deg,var(--ink-soft),var(--art-grey));opacity:.75}
  .art--illustration{background:radial-gradient(ellipse,var(--art-tan),rgba(168,149,122,.25) 75%,transparent)}
  .art--flourish{background:linear-gradient(90deg,transparent,var(--rule),transparent);height:14px;opacity:.6}

  .section-head{position:absolute;display:flex;align-items:center;gap:8px;white-space:nowrap;
    font-family:"Passion One",Impact,sans-serif;font-weight:700;font-size:36px;line-height:1;color:var(--ink);letter-spacing:.5px}
  .section-head svg{flex:none}
  .section-head--small{font-size:22px}

  .item-list{position:absolute;list-style:none;font-weight:700;font-size:14.5px;line-height:19px}
  .item-list li{display:flex;justify-content:space-between;gap:14px;white-space:nowrap}
  .item-list li.item-note{font-weight:400;font-size:12.5px;line-height:14px}

  .body-note{position:absolute;font-size:13px;line-height:16px}
  .divider{position:absolute;height:12px}

  .spud{position:absolute;width:300px;font-size:12.5px;line-height:14px}
  .spud-title{display:flex;gap:28px;white-space:nowrap;font-weight:700;font-size:15px;line-height:19px}

  .beef-note{position:absolute;font-weight:700;font-size:13px;letter-spacing:.3px;white-space:nowrap}

  .brand-mark{position:absolute;display:flex;align-items:center;gap:8px;white-space:nowrap;
    font-family:"Passion One",Impact,sans-serif;font-weight:700;font-size:26px;color:var(--ink)}
  .brand-mark .ring{width:24px;height:24px;border:3px solid var(--ink);border-radius:50%}
</style>
</head>
<body>

<section class="menu-page menu-page--front" aria-label="Menu front">
  <div class="wood-band wood-band--top" role="img" aria-label="Weathered wood plank background"></div>
  <div class="wood-band wood-band--bottom" role="img" aria-label="Weathered wood plank background"></div>
  <div class="paper">
    <div class="paper-frame"></div>

    <div class="art art--lettering" style="left:38px;top:35px;width:125px;height:72px" role="img" aria-label="Ornate hand-lettered word Menu"></div>

    <h2 class="section-head" style="left:205px;top:45px">
      <svg width="26" height="22" viewBox="0 0 26 22" aria-hidden="true"><path d="M2 10a11 8 0 0 1 22 0z" fill="var(--ink-soft)"/><rect x="2" y="12" width="22" height="3" fill="var(--ink-soft)"/><path d="M2 17h22a3 3 0 0 1-3 3H5a3 3 0 0 1-3-3z" fill="var(--ink-soft)"/></svg>
      BURGERS
    </h2>
    <ul class="item-list" style="left:205px;top:95px;width:270px">
      <li><span>Snack Burger</span><span>$3.49</span></li>
      <li><span>Snack Cheeseburger</span><span>$3.99</span></li>
      <li><span>Juniper's signature Burger</span><span>$4.99</span></li>
      <li><span>Juniper's signature Cheeseburger</span><span>$5.49</span></li>
    </ul>
    <p class="body-note" style="left:205px;top:180px;width:285px">Burger toppings: bacon, lettuce, tomato, onion, pickle, grilled onions, grilled mushrooms, grilled green peppers, jalapeño peppers.</p>

    <div class="art art--illustration" style="left:100px;top:140px;width:85px;height:90px" role="img" aria-label="Sketch of a wedge of Swiss cheese"></div>

    <svg class="divider" style="left:70px;top:262px" width="400" height="12" aria-hidden="true"><line x1="0" y1="6" x2="400" y2="6" stroke="var(--rule)" stroke-width="1.5"/><path d="M0 6l8-4v8zM400 6l-8-4v8z" fill="var(--rule)"/></svg>
    <div class="art art--flourish" style="left:215px;top:278px;width:110px" role="img" aria-label="Decorative scroll flourish"></div>

    <p class="section-head section-head--small" style="left:60px;top:318px">AND</p>
    <h2 class="section-head" style="left:60px;top:345px">
      <svg width="30" height="16" viewBox="0 0 30 16" aria-hidden="true"><rect x="1" y="4" width="28" height="10" rx="5" fill="var(--ink-soft)"/><rect x="3" y="2" width="24" height="6" rx="3" fill="var(--art-tan)"/></svg>
      DOGS
    </h2>
    <ul class="item-list" style="left:60px;top:395px;width:230px">
      <li><span>Hot Dog</span><span>$2.99</span></li>
      <li><span>Bacon Cheese Hot Dog</span><span>$3.99</span></li>
      <li><span>Slaw Dog</span><span>$3.99</span></li>
      <li><span>Kraut Dog</span><span>$3.49</span></li>
      <li><span>Chili Dog</span><span>$3.99</span></li>
      <li class="item-note">(with or without cheese)</li>
    </ul>
    <p class="beef-note" style="left:65px;top:522px">✶ HOT DOGS ARE 100% BEEF ✶</p>

    <div class="art art--illustration" style="left:310px;top:345px;width:165px;height:95px" role="img" aria-label="Sketch of a grazing cow"></div>

    <div class="brand-mark" style="left:368px;top:500px"><span class="ring"></span>Juniper's</div>
  </div>
  <p class="band-name">Burgers &amp; Dogs</p>
</section>

<section class="menu-page menu-page--back" aria-label="Menu back">
  <div class="wood-band wood-band--top" role="img" aria-label="Weathered wood plank background"></div>
  <div class="wood-band wood-band--bottom" role="img" aria-label="Weathered wood plank background"></div>
  <div class="paper">
    <div class="paper-frame"></div>

    <div class="art art--lettering" style="left:38px;top:35px;width:125px;height:72px" role="img" aria-label="Ornate hand-lettered word Menu"></div>

    <h2 class="section-head" style="left:185px;top:50px">
      <svg width="40" height="18" viewBox="0 0 40 18" aria-hidden="true"><ellipse cx="10" cy="10" rx="9" ry="7" fill="var(--art-tan)"/><ellipse cx="29" cy="9" rx="10" ry="7" fill="var(--ink-soft)"/></svg>
      LOADED POTATOS
    </h2>
    <div class="spud" style="left:185px;top:98px">
      <p class="spud-title"><span>The Plain Tater:</span><span>$4.99</span></p>
      <p>choose from: butter, sour cream, cheese, chives</p>
    </div>
    <div class="spud" style="left:185px;top:138px">
      <p class="spud-title"><span>The Garden Tater:</span><span>$5.99</span></p>
      <p>choose from: the Basic plus, broccoli &amp; cheese, grilled mushrooms, onions, &amp; peppers</p>
    </div>
    <div class="spud" style="left:185px;top:192px">
      <p class="spud-title"><span>The Rancher Tater:</span><span>$6.99</span></p>
      <p>choose from the Basic/Veggie plus: grilled chicken, chili, Philly cheesesteak, pulled pork</p>
    </div>

    <div class="art art--illustration" style="left:90px;top:130px;width:80px;height:120px" role="img" aria-label="Sketch of a fork, knife and spoon"></div>

    <svg class="divider" style="left:70px;top:262px" width="400" height="12" aria-hidden="true"><line x1="0" y1="6" x2="400" y2="6" stroke="var(--rule)" stroke-width="1.5"/><path d="M0 6l8-4v8zM400 6l-8-4v8z" fill="var(--rule)"/></svg>
    <div class="art art--flourish" style="left:215px;top:278px;width:110px" role="img" aria-label="Decorative scroll flourish"></div>

    <h2 class="section-head" style="left:60px;top:305px">
      <svg width="26" height="20" viewBox="0 0 26 20" aria-hidden="true"><path d="M2 9L13 2l11 7z" fill="var(--ink-soft)"/><rect x="2" y="10" width="22" height="4" fill="var(--art-tan)"/><rect x="2" y="15" width="22" height="4" rx="1" fill="var(--ink-soft)"/></svg>
      OTHER
    </h2>
    <ul class="item-list" style="left:60px;top:355px;width:300px">
      <li><span>Grilled Chicken Sandwich</span><span>$5.99</span></li>
      <li><span>Grilled Chicken Sandwich with cheese</span><span>$6.49</span></li>
      <li class="item-note">(Same toppings as burgers)</li>
    </ul>

    <h2 class="section-head" style="left:60px;top:422px">
      <svg width="22" height="30" viewBox="0 0 22 30" aria-hidden="true"><path d="M5 2v12M9 1v13M13 2v12M17 1v13" stroke="var(--art-tan)" stroke-width="3"/><path d="M2 12h18l-3 16H5z" fill="var(--ink-soft)"/></svg>
      FRENCH FRIES
    </h2>
    <p class="item-list" style="left:315px;top:440px">$1.99</p>

    <h2 class="section-head" style="left:60px;top:462px">
      <svg width="22" height="30" viewBox="0 0 22 30" aria-hidden="true"><path d="M12 0v6" stroke="var(--ink-soft)" stroke-width="2"/><rect x="3" y="5" width="16" height="4" fill="var(--ink-soft)"/><path d="M4 10h14l-2 18H6z" fill="var(--art-tan)"/></svg>
      DRINKS
    </h2>
    <ul class="item-list" style="left:60px;top:510px;width:150px">
      <li><span>32oz. Drink</span><span>$1.88</span></li>
      <li><span>20oz. Drink</span><span>$1.69</span></li>
    </ul>

    <div class="art art--illustration" style="left:385px;top:315px;width:55px;height:160px" role="img" aria-label="Sketch of a stalk of wheat"></div>

    <div class="brand-mark" style="left:368px;top:500px"><span class="ring"></span>Juniper's</div>
  </div>
  <p class="band-name">Burgers &amp; Dogs</p>
</section>

</body>
</html>
```